High value cover design for an A4 ideation pad.

The product is NOT A BOOK.

It's an A4 ideation pad for professionals, designers and creators who handwrite their ideas. Visualise creators like Paul Menteith, Glen Usborne and Carl Whitmoor in your mind's eye.

I'm looking for a cover design for the ideation pad. Both front and back.

It should look, feel and convey the following.

--> A handcrafted product experience

--> High value & Elegance

--> Inspiration

Mandatory --> See Uploaded Files --> Files 1, 5 & 6

Target Market(s)

- Designers

-Creative Professionals

- Entrepreneurs

who handwrite their ideas. Visualise creators like Paul Menteith, Glen Usborne and Carl Whitmoor in your mind's eye.

Industry/Entity Type

Stationary

Font styles to use
Script
Other font styles liked:
• Calligraphy

Colors
fbed22

Requirements
Must have
• Title text - Ink And Iron

-Text in gold on brown leather background to convey high value for the front cover.

--> High value & Elegance

--> Inspiration

--> Should compel the customers to pick up and own the idea pad
Nice to have
• That's my take but other ideas are welcome
Should not have
• Must not convey

- low value

```html
<!DOCTYPE html>
<html lang="en">
<head>
<meta charset="utf-8">
<title>Ink And Iron — Ideation Pad Cover</title>
<link rel="stylesheet" href="https://fonts.googleapis.com/css2?family=Great+Vibes&display=swap">
<style>
  :root {
    --backdrop: #e9e9ea;
    --cover: #161718;
    --cover-edge: #0c0d0e;
    --pattern: #1f2122;
    --pattern-line: #2a2c2e;
    --gold: #e2ad45;
    --gold-light: #f3cf72;
    --gold-deep: #b98426;
  }
  * { box-sizing: border-box; margin: 0; padding: 0; }
  html, body {
    width: 1200px;
    height: 900px;
    overflow: hidden;
    background: var(--backdrop);
  }
  .spread {
    position: relative;
    width: 1200px;
    height: 900px;
    display: flex;
    align-items: center;
    justify-content: center;
    gap: 40px;
  }
  .cover {
    position: relative;
    width: 540px;
    height: 420px;
    background: var(--cover);
    border-radius: 4px;
    box-shadow: 0 18px 40px rgba(0,0,0,0.25), inset 0 0 0 1px var(--cover-edge);
    overflow: hidden;
  }
  /* front cover */
  .leaf-frame {
    position: absolute;
    left: 40px;
    top: 40px;
    width: 460px;
    height: 340px;
    background:
      repeating-linear-gradient(135deg, var(--pattern) 0 14px, var(--pattern-line) 14px 16px);
    border-radius: 2px;
  }
  .leaf-frame::after {
    content: "";
    position: absolute;
    inset: 60px;
    background: var(--cover);
  }
  .corner-mark {
    position: absolute;
    width: 16px;
    height: 16px;
    border-color: var(--gold);
    border-style: solid;
    border-width: 0;
  }
  .corner-mark--left   { left: 118px; top: 202px; border-left-width: 2px; border-bottom-width: 2px; transform: rotate(45deg); }
  .corner-mark--right  { right: 118px; top: 202px; border-right-width: 2px; border-top-width: 2px; transform: rotate(45deg); }
  .corner-mark--top    { left: 262px; top: 112px; border-left-width: 2px; border-top-width: 2px; transform: rotate(45deg); }
  .corner-mark--bottom { left: 262px; bottom: 112px; border-right-width: 2px; border-bottom-width: 2px; transform: rotate(45deg); }
  .feather-art {
    position: absolute;
    left: 200px;
    top: 128px;
    width: 140px;
    height: 120px;
    border-radius: 50% 50% 50% 50% / 60% 60% 40% 40%;
    background: radial-gradient(ellipse at 40% 40%, var(--gold-light), var(--gold) 55%, var(--gold-deep));
    opacity: 0.9;
  }
  .title {
    position: absolute;
    left: 0;
    right: 0;
    top: 250px;
    text-align: center;
    font-family: "Great Vibes", cursive;
    font-size: 40px;
    font-weight: 400;
    color: var(--gold);
    line-height: 1;
  }
  /* back cover */
  .ink-splash {
    position: absolute;
    right: 56px;
    top: 70px;
    width: 46px;
    height: 40px;
    border-radius: 50%;
    background: radial-gradient(circle at 40% 40%, var(--gold-light), var(--gold) 60%, var(--gold-deep));
  }
</style>
</head>
<body>
  <main class="spread">
    <section class="cover cover--front" aria-label="Front cover">
      <div class="leaf-frame" role="img" aria-label="Embossed leaf pattern border"></div>
      <span class="corner-mark corner-mark--top"></span>
      <span class="corner-mark corner-mark--left"></span>
      <span class="corner-mark corner-mark--right"></span>
      <span class="corner-mark corner-mark--bottom"></span>
      <div class="feather-art" role="img" aria-label="Gold foil quill feather illustration"></div>
      <h1 class="title">Ink And Iron</h1>
    </section>
    <section class="cover cover--back" aria-label="Back cover">
      <div class="ink-splash" role="img" aria-label="Gold ink drop splash with quill nib"></div>
    </section>
  </main>
</body>
</html>
```